Inviting A6 Flyer for Church membership

We need an A6 size flyer for the church. We are looking for something fresh, inviting and impactful. Church new logo and current flyer design attached.
Back text as follows:
We would love to have you join us as our SPECIAL GUEST this Sunday at 10am.
You can find us at Harvest Gateway Family Church, 17-19 Meadowbrook Lane
(Behind Farley), Pellham Brook Village,KL7 2RT
For more information or for a chat, please call us on 07614 290457 / 07781 504316 or email church@hgfcuk.org
Target Market(s)
Church
Industry/Entity Type
Church
Colors
Designer to choose colors to be used in the design.
Requirements
Must have
- fresh, inviting and impactful.
- Chruch logo (attached)
Should not have
- Too much going on

```html
<!DOCTYPE html>
<html lang="en">
<head>
<meta charset="utf-8">
<title>Harvest Gateway – Be Our Special Guest</title>
<link href="https://fonts.googleapis.com/css2?family=Lobster&family=Josefin+Slab:wght@400;600&display=swap" rel="stylesheet">
<style>
  :root {
    --page: #7e7e7e;
    --teal: #3f6a78;
    --teal-dark: #1f3a40;
    --field-dark: #1c2620;
    --field-mid: #2c3a2e;
    --white: #ffffff;
    --sky-blue: #2f6e86;
  }
  * { margin: 0; padding: 0; box-sizing: border-box; }
  html, body { width: 880px; height: 1200px; overflow: hidden; }
  body { background: var(--page); position: relative; }

  .card {
    position: absolute;
    left: 98px;
    width: 684px;
    height: 484px;
    overflow: hidden;
    box-shadow: 0 6px 22px rgba(0,0,0,0.45);
  }
  .card--front { top: 78px; }
  .card--back { top: 636px; }

  /* Front */
  .front-sky {
    position: absolute; left: 0; top: 0; width: 100%; height: 242px;
    background: linear-gradient(to bottom, #4f7a84 0%, #a9c0c4 35%, #f3f6f6 70%, #ffffff 100%);
  }
  .front-field {
    position: absolute; left: 0; top: 242px; width: 100%; height: 242px;
    background: linear-gradient(to bottom, var(--field-mid) 0%, var(--field-dark) 60%, #141a16 100%);
  }
  .frame-top {
    position: absolute; left: 12px; top: 13px; width: 660px; height: 235px;
    border: 5px solid var(--teal); border-bottom: none;
  }
  .frame-bottom {
    position: absolute; left: 12px; top: 242px; width: 660px; height: 230px;
    border: 5px solid var(--white); border-top: none;
  }
  .brand {
    position: absolute; left: 0; top: 150px; width: 100%; text-align: center;
    font-family: 'Josefin Slab', serif; font-weight: 600; color: var(--teal-dark);
    font-size: 30px; line-height: 34px; letter-spacing: 1px;
  }
  .headline {
    position: absolute; left: 0; width: 100%; text-align: center;
    font-family: 'Lobster', cursive; font-weight: 400; color: var(--white);
  }
  .headline--top { top: 262px; font-size: 80px; letter-spacing: 3px; }
  .headline--bottom { top: 362px; font-size: 72px; }

  /* Back */
  .back-photo {
    position: absolute; inset: 0;
    background:
      radial-gradient(ellipse at 45% 35%, var(--sky-blue) 0%, #1f4550 45%, transparent 80%),
      linear-gradient(to right, #a88766 0%, var(--teal-dark) 18%, var(--teal-dark) 82%, #b0906e 100%);
  }
  .back-panel {
    position: absolute; left: 22px; top: 22px; width: 640px; height: 440px;
    background: rgba(20, 44, 50, 0.55);
  }
  .back-frame {
    position: absolute; left: 12px; top: 12px; width: 660px; height: 460px;
    border: 5px solid var(--white);
  }
  .details {
    position: absolute; left: 0; top: 96px; width: 100%; text-align: center;
    font-family: 'Josefin Slab', serif; color: var(--white);
    font-size: 24px; line-height: 31px; letter-spacing: 0.8px;
  }
  .details p + p { margin-top: 31px; }
  .details strong { font-weight: 600; }
</style>
</head>
<body>
  <section class="card card--front">
    <div class="front-sky" role="img" aria-label="Misty teal sky fading to white"></div>
    <div class="front-field" role="img" aria-label="Dark photo of tall grass in a field"></div>
    <div class="frame-top"></div>
    <div class="frame-bottom"></div>
    <div class="brand">Harvest Gateway Ministries</div>
    <h1 class="headline headline--top">Be Our</h1>
    <h2 class="headline headline--bottom">Special Guest</h2>
  </section>

  <section class="card card--back">
    <div class="back-photo" role="img" aria-label="Blurred photo of grass against a teal evening sky with warm light at the edges"></div>
    <div class="back-panel"></div>
    <div class="back-frame"></div>
    <div class="details">
      <p>We would love to have you join us as our<br><strong>SPECIAL GUEST</strong> this Sunday at 10am.</p>
      <p>You can find us at Harvest Gateway Family<br>Church, 17-19 Meadowbrook Lane<br>(Behind Farley), Pellham Brook Village,KL7 2RT</p>
      <p>For more information or for a chat, please<br>call us on <strong>07614 290457 / 07781 504316</strong><br>or email <strong>church@hgfcuk.org</strong></p>
    </div>
  </section>
</body>
</html>
```